Young Adult Retreat Needs Event Promo Graphics

I need graphics designed for our summer young adult (18 years old - 30 years old) camp-style retreat. This event will take place at a campground in the black hills of South Dakota. Primary graphic design is for a 11x17 poster but will also need the images resized for:

-social media: square; can include only main titles or main titles and speaker
-16x9 title slide that includes: titles, full background images, organization logo, and website. No camp speaker or dates, no additional info.
- a postcard size (4.25in x 6in) with all content on it

All graphics need to be print quality (300 dpi or higher)

11x17 main poster design should include the following:
-Main Title: PR Brightway (or logo) presents . . . South Dakota Young Adult Retreat
-Dates: June 3-5th, 2022
-Register at PRBrightway.com
-Cedar Ridge Lodge Center, Deadwood, SD
-Speaker: Marla Pettigrew (photo attached)
-Include PR Brightway logo
-Event Graphic should be attractive to 18-30 year olds but SHOULD NOT include references to alcohol, sexuality, drugs, or profanity.

My graphic design experience is limited. I will need help receiving the files I need in the various sizes. Thank you.

```html
<!DOCTYPE html>
<html lang="en">
<head>
<meta charset="utf-8">
<title>South Dakota Young Adult Retreat – Promo Set</title>
<link rel="stylesheet" href="https://fonts.googleapis.com/css2?family=Londrina+Solid:wght@400;900&family=Open+Sans:wght@400&family=Poiret+One&family=PT+Sans+Narrow:wght@400;700&display=swap">
<style>
  :root {
    --ink: #1c1620;
    --venue-ink: #2b1530;
    --logo-blue: #1d7fd6;
    --speaker-purple: #a0308f;
    --speaker-name: #8b1579;
    --title-top-a: #861170;
    --title-top-b: #d4186c;
    --retreat-a: #f3166f;
    --retreat-b: #ff6c3c;
    --sky-lilac: #b9a6dc;
    --sky-pink: #f6c3e0;
    --sky-glow: #ffffff;
    --band-pink: #ee93c8;
    --band-violet: #c58ad8;
    --photo-pink: #e989c6;
    --photo-warm: #b98a7a;
    --label: #111111;
  }
  * { margin: 0; padding: 0; box-sizing: border-box; }
  html, body { width: 1200px; height: 1013px; overflow: hidden; background: #ffffff; }
  body { position: relative; }

  .artboard { position: absolute; overflow: hidden; }
  .artboard--square { left: 16px; top: 12px; width: 463px; height: 463px; }
  .artboard--slide { left: 501px; top: 13px; width: 674px; height: 352px; }
  .artboard--postcard { left: 513px; top: 462px; width: 669px; height: 474px; }

  .sky {
    position: absolute; inset: 0;
    background:
      radial-gradient(circle at 28% 10%, var(--sky-glow) 0, rgba(255,255,255,0.85) 8%, rgba(255,255,255,0) 32%),
      radial-gradient(ellipse at 55% 70%, rgba(255,240,248,0.9) 0, rgba(255,240,248,0) 55%),
      radial-gradient(ellipse at 90% 20%, rgba(157,134,208,0.8) 0, rgba(157,134,208,0) 45%),
      radial-gradient(ellipse at 10% 55%, rgba(170,150,215,0.7) 0, rgba(170,150,215,0) 40%),
      linear-gradient(180deg, var(--sky-lilac) 0%, #e6d6ef 45%, var(--sky-pink) 100%);
  }
  .artboard--postcard .sky {
    background:
      radial-gradient(circle at 28% 6%, var(--sky-glow) 0, rgba(255,255,255,0.85) 8%, rgba(255,255,255,0) 30%),
      radial-gradient(ellipse at 55% 55%, rgba(255,240,248,0.9) 0, rgba(255,240,248,0) 50%),
      radial-gradient(ellipse at 92% 20%, rgba(157,134,208,0.8) 0, rgba(157,134,208,0) 45%),
      linear-gradient(180deg, var(--sky-lilac) 0%, #eadcf0 40%, #f7e2ef 68%, #c9a6e2 76%, #d77fc8 88%, #e65fa5 100%);
  }

  .brand {
    position: absolute; display: flex; align-items: center; gap: 6px;
    font-family: "PT Sans Narrow", sans-serif; white-space: nowrap;
  }
  .brand__name { font-weight: 700; color: var(--logo-blue); }
  .brand__presents { font-weight: 400; color: var(--ink); text-transform: uppercase; }

  .artboard--square .brand { left: 190px; top: 10px; }
  .artboard--square .brand__name { font-size: 17px; }
  .artboard--square .brand__presents { font-size: 10px; }
  .artboard--slide .brand { left: 18px; top: 22px; }
  .artboard--slide .brand__name { font-size: 22px; }
  .artboard--slide .brand__presents { font-size: 13px; }
  .artboard--postcard .brand { right: 14px; top: 22px; }
  .artboard--postcard .brand__name { font-size: 19px; }
  .artboard--postcard .brand__presents { font-size: 11px; }

  .state {
    position: absolute; white-space: nowrap; transform: translateX(-50%);
    font-family: "Poiret One", sans-serif; color: var(--ink); word-spacing: 0.15em;
  }
  .title-line {
    position: absolute; white-space: nowrap; line-height: 1;
    transform: translateX(-50%) scaleX(var(--sx, 0.72));
    font-family: "Londrina Solid", sans-serif; font-weight: 900;
    -webkit-background-clip: text; background-clip: text; color: transparent;
    letter-spacing: 0.02em; word-spacing: 0.12em;
  }
  .title-line--young { background-image: linear-gradient(90deg, var(--title-top-a), var(--title-top-b)); }
  .title-line--retreat { background-image: linear-gradient(180deg, var(--retreat-a), var(--retreat-b)); }

  .date { position: absolute; font-family: "Poiret One", sans-serif; color: var(--ink); white-space: nowrap; word-spacing: 0.12em; }

  .speaker-photo {
    position: absolute; border-radius: 50%;
    background: radial-gradient(circle at 50% 55%, var(--photo-warm) 0, #c98fa8 45%, var(--photo-pink) 100%);
  }

  .speaker { position: absolute; font-family: "PT Sans Narrow", sans-serif; white-space: nowrap; }
  .speaker__label { color: var(--speaker-purple); font-weight: 400; }
  .speaker__name { color: var(--speaker-name); font-weight: 700; text-transform: uppercase; }

  .venue-band {
    position: absolute; left: 0; right: 0; bottom: 0; height: 40px;
    display: flex; align-items: center; justify-content: space-between; padding: 0 17px 0 10px;
    background: linear-gradient(90deg, var(--band-violet), var(--band-pink) 50%, var(--band-violet));
    font-family: "PT Sans Narrow", sans-serif; color: var(--venue-ink); white-space: nowrap;
  }
  .venue-band__place { font-weight: 700; font-size: 17px; }
  .venue-band__register { font-size: 14px; }

  .website { position: absolute; left: 0; right: 0; text-align: center; font-family: "PT Sans Narrow", sans-serif; color: var(--ink); }

  .details { position: absolute; left: 194px; width: 280px; text-align: center; font-family: "PT Sans Narrow", sans-serif; color: var(--venue-ink); }
  .details__place { font-weight: 700; font-size: 21px; line-height: 28px; }
  .details__register { font-size: 17px; line-height: 24px; margin-top: 4px; }

  .label { position: absolute; font-family: "Open Sans", sans-serif; color: var(--label); white-space: nowrap; transform: translateX(-50%); }
</style>
</head>
<body>

  <section class="artboard artboard--square">
    <div class="sky" role="img" aria-label="Soft pastel sky with clouds, sun glow and lens flare"></div>
    <div class="brand"><span class="brand__name">PR Brightway</span><span class="brand__presents">Presents</span></div>
    <div class="state" style="left:231px; top:52px; font-size:38px;">South Dakota</div>
    <div class="title-line title-line--young" style="left:232px; top:98px; font-size:82px; --sx:0.74;">YOUNG ADULT</div>
    <div class="title-line title-line--retreat" style="left:251px; top:173px; font-size:120px; --sx:0.67;">RETREAT</div>
    <div class="date" style="left:146px; top:290px; font-size:28px;">June 3-5th, 2022</div>
    <div class="speaker-photo" role="img" aria-label="Portrait photo of speaker Marla Pettigrew" style="left:2px; top:273px; width:148px; height:148px;"></div>
    <div class="speaker" style="left:154px; top:358px; font-size:18px;"><span class="speaker__label">Speaker:</span> <span class="speaker__name">Marla Pettigrew</span></div>
    <div class="venue-band">
      <span class="venue-band__place">Cedar Ridge Lodge Center, Deadwood, SD</span>
      <span class="venue-band__register">Register at PRBrightway.com</span>
    </div>
  </section>
  <div class="label" style="left:247px; top:487px; font-size:30px;">instagram 1080x1080</div>

  <section class="artboard artboard--slide">
    <div class="sky" role="img" aria-label="Soft pastel sky with clouds, sun glow and lens flare"></div>
    <div class="brand"><span class="brand__name">PR Brightway</span><span class="brand__presents">Presents</span></div>
    <div class="state" style="left:337px; top:34px; font-size:42px;">South Dakota</div>
    <div class="title-line title-line--young" style="left:335px; top:89px; font-size:97px; --sx:0.77;">YOUNG ADULT</div>
    <div class="title-line title-line--retreat" style="left:355px; top:173px; font-size:137px; --sx:0.71;">RETREAT</div>
    <div class="website" style="top:313px; font-size:23px;">www. PRBrightway.com</div>
  </section>
  <div class="label" style="left:838px; top:389px; font-size:30px;">16:9</div>

  <section class="artboard artboard--postcard">
    <div class="sky" role="img" aria-label="Pastel sky fading into a pink and violet forested valley"></div>
    <div class="brand"><span class="brand__name">PR Brightway</span><span class="brand__presents">Presents</span></div>
    <div class="state" style="left:338px; top:38px; font-size:42px;">South Dakota</div>
    <div class="title-line title-line--young" style="left:334px; top:94px; font-size:96px; --sx:0.76;">YOUNG ADULT</div>
    <div class="title-line title-line--retreat" style="left:354px; top:182px; font-size:140px; --sx:0.68;">RETREAT</div>
    <div class="date" style="left:234px; top:320px; font-size:32px;">June 3-5th, 2022</div>
    <div class="speaker" style="left:4px; width:150px; top:198px; text-align:center; line-height:26px;">
      <div class="speaker__label" style="font-size:20px;">Speaker:</div>
      <div class="speaker__name" style="font-size:19px;">Marla Pettigrew</div>
    </div>
    <div class="speaker-photo" role="img" aria-label="Portrait photo of speaker Marla Pettigrew" style="left:1px; top:258px; width:175px; height:175px;"></div>
    <div class="details" style="top:381px;">
      <div class="details__place">Cedar Ridge Lodge Center,<br>Deadwood, SD</div>
      <div class="details__register">Register at PRBrightway.com</div>
    </div>
  </section>
  <div class="label" style="left:832px; top:960px; font-size:32px;">postcard 4.25in x 6in</div>

</body>
</html>
```